Lantern Business Cards

Need business cards for my employees at my restaurant.

Needs to include:
Our Logo
Lantern Bowls & Brews
Name: Nora Pettigrew
Title : Owner
Address: 487 Mirella Ave. Kestrel Harbor, OR 86519
Web: www.lanternkestrel.com
Phone: 399-555-0147
Cell: 399-555-0192
Email: info@lanternkestrel.com

```html
<!DOCTYPE html>
<html lang="en">
<head>
<meta charset="utf-8">
<title>Lantern Business Cards</title>
<link href="https://fonts.googleapis.com/css2?family=Nunito+Sans:wght@400;600;800&display=swap" rel="stylesheet">
<style>
  :root {
    --red: #be2030;
    --black: #000000;
    --charcoal: #1b1b1b;
    --paper: #ffffff;
    --ink: #1a1a1a;
    --backdrop: #e7e7e9;
  }
  * { margin: 0; padding: 0; box-sizing: border-box; }
  html, body { width: 1200px; height: 1108px; overflow: hidden; }
  body {
    background: var(--backdrop);
    font-family: "Nunito Sans", sans-serif;
    position: relative;
  }
  .card { position: absolute; overflow: hidden; }
  .card-front { left: 219px; top: 50px; width: 775px; height: 473px; background: var(--paper); }
  .card-back { left: 217px; top: 568px; width: 777px; height: 456px; background: var(--charcoal); }

  .brand {
    position: absolute;
    display: flex; flex-direction: column; align-items: center;
    text-align: center;
  }
  .brand-dot { border-radius: 50%; background: var(--red); }
  .brand-name {
    color: var(--red);
    font-weight: 800;
    text-transform: uppercase;
    line-height: 1.05;
    letter-spacing: 1px;
    white-space: nowrap;
  }
  .card-front .brand { left: 50px; top: 135px; width: 340px; }
  .card-front .brand-dot { width: 70px; height: 70px; margin-bottom: 18px; }
  .card-front .brand-name { font-size: 30px; }

  .card-back .brand { left: 88px; top: 110px; width: 600px; }
  .card-back .brand-dot { width: 110px; height: 110px; margin-bottom: 26px; }
  .card-back .brand-name { font-size: 46px; }

  .divider { position: absolute; left: 389px; top: 126px; width: 2px; height: 232px; background: var(--red); }

  .contact { position: absolute; left: 409px; top: 122px; color: var(--ink); }
  .contact-name { color: var(--red); font-weight: 800; font-size: 29px; line-height: 1.1; }
  .contact-title { font-size: 18px; line-height: 1.2; margin-bottom: 18px; }
  .contact-address { font-size: 18px; line-height: 1.2; margin-bottom: 12px; padding-left: 2px; }
  .contact-list { list-style: none; font-size: 18px; line-height: 1; }
  .contact-list li { display: flex; align-items: center; gap: 9px; height: 25px; }
  .contact-list svg { width: 20px; height: 18px; fill: var(--red); flex: none; }

  .band { position: absolute; left: 0; bottom: 0; width: 775px; height: 34px; }
</style>
</head>
<body>
  <section class="card card-front">
    <div class="brand">
      <span class="brand-dot"></span>
      <span class="brand-name">Lantern<br>Bowls &amp; Brews</span>
    </div>
    <div class="divider"></div>
    <div class="contact">
      <p class="contact-name">Nora Pettigrew</p>
      <p class="contact-title">Owner</p>
      <p class="contact-address">487 Mirella Ave.<br>Kestrel Harbor, OR 86519</p>
      <ul class="contact-list">
        <li><svg viewBox="0 0 20 20"><path d="M4 1l4 4-2 3c1 3 3 5 6 6l3-2 4 4-3 3C8 19 1 12 1 4z"/></svg>399-555-0192</li>
        <li><svg viewBox="0 0 20 20"><path d="M1 6c0-3 18-3 18 0v2h-4V6H5v2H1z"/><path d="M4 9h12l2 9H2z"/></svg>399-555-0147</li>
        <li><svg viewBox="0 0 20 16"><path d="M1 2h18v12H1z M2 3l8 6 8-6" fill="none" stroke="#be2030" stroke-width="2"/></svg>info@lanternkestrel.com</li>
        <li><svg viewBox="0 0 20 20"><circle cx="10" cy="10" r="9"/></svg>www.lanternkestrel.com</li>
      </ul>
    </div>
    <svg class="band" viewBox="0 0 775 34" preserveAspectRatio="none">
      <polygon points="0,0 383,0 361,34 0,34" fill="#000"/>
      <polygon points="390,0 775,0 775,34 368,34" fill="#be2030"/>
    </svg>
  </section>

  <section class="card card-back">
    <div class="brand">
      <span class="brand-dot"></span>
      <span class="brand-name">Lantern<br>Bowls &amp; Brews</span>
    </div>
  </section>
</body>
</html>
```